Bref créative
Delivery Flyer, To-Go Menu and Dine-In Menu for Restaurant
Lotus Quill Restaurant
Food/Restaurant
1) 8.5x11 Delivery Flyer - Will need to incorporate restaurant logo and logo/details of delivery service we partnered with (see www.lotusquill-bnv.example/delivery). Will also need to conform to NMCR (National Mail Courier Registry) layout (i.e. include small postage-stamp area and address-box area). Full Lunch and Dinner menu to be included.
2) To-Go Menu – To-Go menu to be handed out to customers. Full Lunch and Dinner menu to be included. Will need to incorporate restaurant logo and modern design.
3) Dine-In Menu – a new full menu for our restaurant. Currently, we have them as separate menus (i.e. we have a lunch special menu and a separate dinner menu). Please go to website to download current menus, and incorporate picture gallery into design.
Food
1) 8.5x11 Delivery Flyer – Residential and Businesses. This will be sent as a standalone flyer and should incorporate modern colors and health-focused concept of restaurant.
2) To-Go Menu – Any customer (dine-in, to-go, catering, corporate, etc.) wanting a To-Go menu. Also, needs to incorporate modern colors and health-focused concept of restaurant.
3) Dine-In Menu - Handed out to Dine-In customers only; may be posted online. Also, needs to incorporate modern colors and health-focused concept of restaurant.
**Note: See “Details” section for requirements. Please use PDF versions of Lunch and Dinner Menus AND Food Gallery/Pictures @ www.lotusquill-bnv.example as reference.
AI of the logo
Dinner Menu - MS Word Doc
Lunch Menu - MS Word Doc

```html
<!DOCTYPE html>
<html lang="en">
<head>
<meta charset="utf-8">
<title>Lotus Quill Restaurant – Dine-In Menu</title>
<link href="https://fonts.googleapis.com/css2?family=Open+Sans:wght@400;600;700&family=Great+Vibes&display=swap" rel="stylesheet">
<style>
:root{
  --cream:#fbf2dc;
  --cream-deep:#f5e3bd;
  --wine:#6e0d12;
  --crimson:#9c1a17;
  --orange:#e2561a;
  --amber:#f29a2e;
  --ink:#3a2418;
  --white:#ffffff;
}
*{margin:0;padding:0;box-sizing:border-box}
html,body{width:1200px;height:729px;overflow:hidden;background:var(--cream)}
body{font-family:"Open Sans",Arial,sans-serif;color:var(--ink)}
.menu{position:relative;width:1200px;height:729px;background:linear-gradient(180deg,var(--cream) 0%,var(--cream-deep) 100%);overflow:hidden}

/* left intro panel */
.intro{position:absolute;left:0;top:0;width:222px;height:729px;background:var(--cream)}
.intro-swoosh{position:absolute;left:0;top:0}
.brand{position:absolute;left:14px;top:22px;display:flex;align-items:center;gap:7px}
.brand-dot{width:22px;height:22px;border-radius:50%;background:var(--orange)}
.brand-name{font-weight:700;font-size:20px;color:var(--crimson);letter-spacing:.3px}
.brand-tag{position:absolute;left:44px;top:50px;font-size:8px;font-weight:600;color:var(--orange);letter-spacing:.3px}
.intro-copy{position:absolute;left:12px;top:104px;width:202px;font-size:9.2px;line-height:12.4px;color:var(--ink)}
.intro-photo{position:absolute;left:0;top:432px;width:222px;height:297px;background:linear-gradient(160deg,#f7e9c8 0%,#e9b15a 35%,#c9651f 70%,#7d2a10 100%)}
.intro-slogan{position:absolute;left:14px;top:448px;color:var(--white);text-shadow:0 1px 3px rgba(80,20,0,.45)}
.intro-slogan .big{font-family:"Great Vibes",cursive;font-size:50px;line-height:44px;display:block}
.intro-slogan .small{font-family:"Great Vibes",cursive;font-size:28px;line-height:28px;display:block;padding-left:62px;color:#fff3d6}

/* header */
.masthead{position:absolute;left:222px;top:0}
.menu-title{position:absolute;left:955px;top:14px;font-family:"Great Vibes",cursive;font-size:32px;line-height:36px;color:var(--white);white-space:nowrap}

/* columns */
.col{position:absolute;top:74px;font-size:9.6px;line-height:12.6px}
.col-1{left:283px;width:190px}
.col-2{left:524px;width:268px}
.col-3{left:806px;width:374px;top:62px}
.section{font-weight:700;color:var(--orange);font-size:11.5px;line-height:15px;margin-top:5px}
.section:first-child{margin-top:0}
.row{display:flex;justify-content:space-between;gap:6px}
.row .price{white-space:nowrap}
.note{font-size:8.4px;line-height:11px;color:#6b4a35}
.sub{padding-left:8px}
.prices{color:var(--crimson);font-weight:600}
.price-pair{display:inline-flex;gap:14px}
.w110{width:110px}
.w200{width:200px}
.w300{width:300px}
</style>
</head>
<body>
<main class="menu">

  <svg class="masthead" width="978" height="110" viewBox="0 0 978 110" aria-hidden="true">
    <path d="M0 0H978V42C820 58 700 34 560 50C420 66 260 40 0 62Z" fill="var(--wine)"/>
    <path d="M0 62C260 40 420 66 560 50C700 34 820 58 978 42V52C820 68 700 46 560 60C420 76 260 52 0 74Z" fill="var(--orange)"/>
    <path d="M0 74C260 52 420 76 560 60C700 46 820 68 978 52V57C820 73 700 52 560 66C420 82 260 58 0 80Z" fill="var(--amber)"/>
  </svg>
  <div class="menu-title">Dine-In Menu</div>

  <section class="intro">
    <svg class="intro-swoosh" width="222" height="100" viewBox="0 0 222 100" aria-hidden="true">
      <path d="M0 0H222V6C160 16 90 2 0 12Z" fill="var(--wine)"/>
      <path d="M0 66C90 62 160 80 222 62V72C160 90 90 74 0 78Z" fill="var(--orange)"/>
    </svg>
    <div class="brand"><span class="brand-dot"></span><span class="brand-name">Lotus Quill</span></div>
    <div class="brand-tag">Healthy. Fine Thai Cuisine</div>
    <div class="intro-copy">
      <p>Named one of the best Thai restaurants in Riverbend by the Bexar Valley Courier, loved by food critics, our customers and reviewers on TasteBoard, CityForkr, etc. continue to name us one of the best Thai restaurants in the area.</p>
      <p>We pride ourselves in preparing one of the fastest, freshest, and most flavorful Thai meals for our lunch patrons. Many of our customers appreciate that they can have a great sit down meal and be in-and-out quickly!</p>
      <p>In addition to freshly preparing and serving you a variety of healthy, traditional Thai dishes, the Thai Lotus family is always creating NEW dishes for you, our customers, to enjoy! Throughout the years, you have voted in many of our original dishes into our menu (e.g. Spicy Mango Delight, Lotus Quill Fried Rice, Quill Broccoli, etc.).</p>
    </div>
    <div class="intro-photo" role="img" aria-label="Photograph of a plated Thai dish"></div>
    <div class="intro-slogan"><span class="big">high flavor</span><span class="small">from the<br>best recipes</span></div>
  </section>

  <section class="col col-1">
    <div class="section">Appetizers</div>
    <div class="row"><span>The quill chicken satay (6 skewers)</span><span class="price">5.95</span></div>
    <div class="row"><span>Steamed potstickers (5 pcs) (veggie &amp; pork)</span><span class="price">5.95</span></div>
    <div>Summer roll</div>
    <div class="row sub"><span>- veggie (5 pcs)</span><span class="price">4.15</span></div>
    <div class="row sub"><span>- shrimp (5 pcs)</span><span class="price">4.95</span></div>
    <div>Fried spring roll</div>
    <div class="row sub"><span>- veggie (5 pcs)</span><span class="price">4.15</span></div>
    <div class="row sub"><span>- chicken (5 pcs)</span><span class="price">4.50</span></div>
    <div class="row"><span>Quill crab supreme (5 pcs)</span><span class="price">4.95</span></div>
    <div>(fried crab rangoon)</div>
    <div class="row"><span>Quill platters</span><span class="price">8.50</span></div>
    <div class="note">crab supreme (5 pcs), veggie spring rolls (5 pcs) and veggie summer rolls</div>
    <div class="row"><span>Shrimp parcel (5 pcs)</span><span class="price">4.95</span></div>
    <div>Miang kai</div>
    <div class="row"><span>(chicken lettuce wraps)</span><span class="price">6.95</span></div>
    <div>Spicy cake 3 thru 5 plus</div>
    <div class="note">Add extra meat or shrimp (if) for $2.50, vegetables $1.50</div>

    <div class="section">Soups</div>
    <div>Tom yum</div>
    <div class="row sub"><span>chicken or tofu</span><span class="price-pair"><span>5.25</span><span>10.50</span></span></div>
    <div class="row sub"><span>- shrimp</span><span class="price-pair"><span>6.25</span><span>11.50</span></span></div>
    <div>Tom kha</div>
    <div class="row sub"><span>chicken or tofu</span><span class="price-pair"><span>5.25</span><span>10.50</span></span></div>
    <div class="row sub"><span>- shrimp</span><span class="price-pair"><span>6.25</span><span>11.50</span></span></div>
    <div class="row"><span>Egg drop soup</span><span class="price">2.50</span></div>
    <div class="row"><span>Vegetable soup</span><span class="price">2.50</span></div>
    <div class="note">Carrots, onions, cabbage and celery in a clear broth</div>

    <div class="section">Salads</div>
    <div class="row w110"><span>Thai salad</span><span class="price">4.25</span></div>
    <div class="row sub w110"><span>- chicken</span><span class="price">5.25</span></div>
    <div class="row sub w110"><span>- shrimp</span><span class="price">6.25</span></div>
  </section>

  <section class="col col-2">
    <div class="section">Tom yum</div>
    <div class="prices">Tofu/chicken - 7.95 &nbsp; beef - 8.95 &nbsp; shrimp - 9.50</div>
    <div>Tom yum fried rice</div>
    <div>Tom kha noodles</div>
    <div>Tom yum soup</div>
    <div>(thai spicy glass noodles)</div>
    <div class="row w200"><span>Chicken and shrimp combo</span><span class="price">8.95</span></div>

    <div class="section">Noodle dishes</div>
    <div class="prices">Tofu/chicken - 8.75 &nbsp; beef 9.75 &nbsp; shrimp 10.50</div>
    <div>Pad thai</div>
    <div>Broccoli noodles (pad see ew)</div>
    <div>Drunken (or noodles/khang kao)</div>
    <div>Pad woon sen</div>
    <div>Spicy crispy noodles/pad kee mao</div>
    <div>Mama noodles/gow kaow kua gai</div>
    <div>Rice noodle soup</div>

    <div class="section">Fried rice dishes</div>
    <div class="prices">Tofu/chicken - 8.75 &nbsp; beef 9.75 &nbsp; shrimp 10.50</div>
    <div>Spicy basil fried rice (lotus quill original)</div>
    <div>Pineapple fried rice</div>
    <div>Thai fried rice</div>
    <div>Lotus Quill fried rice</div>

    <div class="section">Stir - fry</div>
    <div class="prices">Tofu/chicken - 8.75 &nbsp; beef 9.75 &nbsp; shrimp 10.50</div>
    <div>Pad prik ped</div>
    <div>Chicken cashew</div>
    <div>Pad sweet sour</div>
    <div>Chicken basil (pad kra prao)</div>
    <div>Chicken ginger (pad king)</div>
    <div>Sweet and sour</div>
    <div>Stir-fried mixed vegetable (pad pak)</div>
    <div>Broccoli chicken</div>
    <div>Lotus Quill broccoli (lotus quill original)</div>
  </section>

  <section class="col col-3">
    <div class="section">Garlic chicken</div>
    <div class="prices">Tofu - 9.25 &nbsp; chicken - 10.25 &nbsp; beef/shrimp (L2) - 11.50</div>

    <div class="section">Thai curry</div>
    <div class="prices">Tofu/chicken - 8.75 &nbsp; beef/shrimp 10.50</div>
    <div>Green curry* (gaeng kiaow waan)</div>
    <div>Golden curry* (gaeng karee)</div>
    <div>Panang curry* (gaeng panang)</div>
    <div>Red curry* (gaeng ped)</div>
    <div class="note">(*note: spicy level 1-5 recommended for curries;<br>lowest ratio level 1-3)</div>

    <div class="section">House specials</div>
    <div>Spicy mango delight (lq original)</div>
    <div class="prices">Tofu/chicken 9.50 &nbsp; beef 10.50 &nbsp; shrimp 11.50</div>
    <div class="section">Quill asparagus (lq original)</div>
    <div class="prices">Tofu/chicken 9.50 &nbsp; beef 10.50 &nbsp; shrimp 11.50</div>
    <div class="row w300"><span>Emerald salmon (lq original)</span><span class="price">12.50</span></div>
    <div class="row w300"><span>Shrimp nuam prik pao</span><span class="price">12.50</span></div>
    <div class="row w300"><span>Steamed fish fillet in spicy lime sauce</span><span class="price">10.50</span></div>
    <div class="row w300"><span>Steamed fish fillet in red sauce</span><span class="price">10.50</span></div>
    <div class="row w300"><span>Lotus Quill seafood supreme</span><span class="price">12.50</span></div>

    <div class="section">Thai tofu</div>
    <div class="prices">Tofu/chicken 8.75 &nbsp; pork/beef 10.75</div>

    <div class="section">Dessert</div>
    <div class="row w300"><span>Sweet sticky rice with mango</span><span class="price">4.50</span></div>
    <div class="row w300"><span>Homemade seasonal fruit ice cream (seasonal availability)</span><span class="price">3.50</span></div>
    <div class="row w300"><span>Homemade coconut ice cream</span><span class="price">2.75</span></div>
    <div class="row w300"><span>Homemade seasonal coconut with sticky rice</span><span class="price">4.50</span></div>
    <div class="row w300"><span>Thai custard with rice</span><span class="price">2.75</span></div>

    <div class="section">Beverages</div>
    <div class="row w300"><span>Fresh lemonade, lemon-lime soda, diet cola, cherry cola</span><span class="price">1.25</span></div>
    <div class="row w300"><span>Hot jasmine tea</span><span class="price">1.25</span></div>
    <div class="row w300"><span>Lemon iced tea (refillable)</span><span class="price">1.75</span></div>
    <div class="row w300"><span>Thai iced tea w/ milk</span><span class="price">2.75</span></div>
  </section>

</main>
</body>
</html>
```